Bref créative
Harborline Motorworks
Business Cards/Stationary
Professional
Marcus Delaney
President
4816 Pell Ave
Detroit, Mi, 48201
mdelaney@harborlinemotorworks.example
www.harborlinemotorworks.example
Use logo I have provided.
Please follow the logos color scheme.
I need business cards, envelopes, company letterhead.
Please try to incorporate my logo somewhere on the back of the card as well.
(WARNING: WHAT BACK OF CARD SAYS COULD BE CHANGED OR SCRAPPED ALL TOGETHER THROUGHOUT THIS PROCESS.)
Dealer Services:
Lead Generation.
Website Development.
Internet Sales Training.
Consumer Services:
Unbiased Vehicle Information
Every Make. Every Model.
At The Lowest Price.

```html
<!DOCTYPE html>
<html lang="en">
<head>
<meta charset="utf-8">
<title>Harborline Motorworks — Stationery</title>
<link href="https://fonts.googleapis.com/css2?family=Arimo:wght@400;700&display=swap" rel="stylesheet">
<style>
:root{
  --red:#c4161c;
  --red-dark:#8e0f13;
  --ink:#1b1b1b;
  --black:#111;
  --grey:#6d6d6d;
  --light:#e6e6e6;
  --paper:#fff;
  --stage:#1c1c1c;
}
*{box-sizing:border-box;margin:0;padding:0}
html,body{width:1200px;height:899px;overflow:hidden}
body{background:var(--stage);font-family:"Arimo",Arial,sans-serif;color:var(--ink);position:relative}
.piece{position:absolute;background:var(--paper);box-shadow:0 4px 10px rgba(0,0,0,.6);overflow:hidden}
.brand{display:flex;align-items:center;gap:4px;font-weight:700;color:var(--ink);white-space:nowrap}
.brand .dot{border-radius:50%;background:var(--red);flex:none}
.tiny{font-size:5px;line-height:8px;color:var(--grey)}
/* letterhead */
.letterhead{left:7px;top:29px;width:224px;height:287px;padding:14px 14px}
.letterhead .brand{font-size:8px}.letterhead .brand .dot{width:10px;height:10px}
.letterhead .body{margin-top:40px;font-size:5px;line-height:8px;color:#444}
.letterhead .body p{margin-bottom:7px}
.letterhead .foot{position:absolute;left:14px;right:14px;bottom:12px;display:flex;justify-content:space-between;align-items:center;border-top:1px solid var(--light);padding-top:5px}
.letterhead .foot .dot{width:14px;height:14px;border-radius:50%;background:var(--red)}
/* folders */
.folder{display:flex;background:none;box-shadow:none;overflow:visible}
.folder .panel{position:relative;flex:1;background:var(--paper);box-shadow:0 4px 10px rgba(0,0,0,.6);overflow:hidden}
.folder .inside{display:flex;flex-direction:column;align-items:center;justify-content:center}
.folder .inside .url{position:absolute;bottom:10%;font-size:7px;color:var(--grey)}
.folder .cover svg{position:absolute;inset:0;width:100%;height:100%}
.folder .cover .brand{position:absolute}
.folder .cover .services{position:absolute;text-align:right;font-size:5px;line-height:7px;color:var(--grey)}
.folder-small{left:243px;top:29px;width:462px;height:287px}
.folder-small .cover .brand{left:10%;top:38%}
.folder-small .cover .services{right:30%;top:60%}
.folder-large{left:491px;top:369px;width:481px;height:292px}
.folder-large .cover .brand{left:22%;top:42%}
.folder-large .cover .services{right:8%;top:60%}
.folder .brand{font-size:9px}.folder .brand .dot{width:13px;height:13px}
/* invoice & fax */
.invoice{padding:12px}
.invoice .head{display:flex;justify-content:space-between;align-items:flex-start}
.invoice .head .brand{font-size:6px}.invoice .head .brand .dot{width:8px;height:8px}
.invoice h2{font-size:14px;color:var(--ink);letter-spacing:1px}
.invoice .bar{height:8px;background:var(--black);margin-top:16px;display:flex;gap:20px;padding-left:6px;font-size:5px;color:#fff;align-items:center}
.invoice .table{margin-top:4px;border:1px solid #bbb;height:55%;display:grid;grid-template-columns:1fr 3fr 1fr 1fr}
.invoice .table div{border-right:1px solid #ddd}
.invoice .total{margin-top:6px;margin-left:auto;width:40%;height:10px;background:var(--light)}
.invoice-small{left:710px;top:29px;width:221px;height:287px}
.invoice-large{left:991px;top:369px;width:185px;height:292px}
.invoice-large .bar{background:var(--red)}
.invoice-large h2{color:var(--red)}
.fax{left:948px;top:29px;width:226px;height:287px;padding:12px}
.fax .head{display:flex;justify-content:space-between;align-items:flex-start}
.fax .brand{font-size:6px}.fax .brand .dot{width:8px;height:8px}
.fax h2{font-size:20px;font-weight:400;color:var(--grey)}
.fax .fields{margin-top:20px;font-size:5px;color:var(--grey);display:grid;grid-template-columns:1fr 1fr;gap:6px}
.fax .fields span{border-bottom:1px solid #ccc;padding-bottom:2px}
.fax .foot{position:absolute;left:12px;right:12px;bottom:10px;height:3px;background:var(--red)}
/* cards */
.card{width:202px;height:110px;border-radius:3px}
.card.round{border-radius:10px}
.card .brand{position:absolute;left:10px;top:10px;font-size:7px}
.card .brand .dot{width:11px;height:11px}
.card .who{position:absolute;right:12px;top:12px;text-align:right}
.card .who b{display:block;font-size:9px;color:var(--red)}
.card .who span{font-size:6px;color:var(--grey)}
.card .contact{position:absolute;left:10px;top:46px;font-size:5px;line-height:8px;color:var(--grey)}
.card .band{position:absolute;left:0;right:0;bottom:0;height:10px;background:linear-gradient(90deg,var(--black),#555)}
.card.back{color:#fff}
.card.back.dark{background:linear-gradient(160deg,#3a3a3a,#0c0c0c)}
.card.back.red{background:linear-gradient(160deg,#d91e24,var(--red-dark))}
.card.back .seal{position:absolute;left:22px;top:22px;width:34px;height:34px;border-radius:50%;background:var(--red);border:2px solid #fff}
.card.back.red .seal{background:var(--black)}
.card.back .list{position:absolute;right:12px;top:14px;text-align:right;font-size:5.5px;line-height:8px}
.card.back .list b{font-size:6px}
.card.back .tag{position:absolute;left:10px;bottom:10px;font-size:5.5px;line-height:8px}
.c1{left:53px}.c2{left:267px}
.r1{top:365px}.r2{top:505px}.r3{top:644px}
/* envelopes */
.envelope{top:680px;width:267px;height:129px}
.envelope .brand{position:absolute;left:10px;top:10px;font-size:7px}.envelope .brand .dot{width:10px;height:10px}
.envelope .seal{position:absolute;left:12px;bottom:10px;width:22px;height:22px;border-radius:50%;background:var(--red)}
.envelope .band{position:absolute;left:0;right:0;bottom:0;height:4px;background:var(--black)}
.env-front{left:498px}
.env-back{left:782px}
.env-back svg{position:absolute;inset:0;width:100%;height:100%}
.env-back .seal{left:50%;top:10px;bottom:auto;margin-left:-9px;width:18px;height:18px}
</style>
</head>
<body>

<section class="piece letterhead">
  <div class="brand"><span class="dot"></span>Harborline Motorworks</div>
  <div class="body">
    <p>Dear Client,</p>
    <p>Thank you for choosing our dealer services. We look forward to a long partnership.</p>
    <p>Our team provides lead generation, website development and sales training for every dealer.</p>
    <p>Sincerely,<br><br>Marcus Delaney<br>President</p>
  </div>
  <div class="foot"><span class="tiny">4816 Pell Ave · Detroit, MI 48201 · www.harborlinemotorworks.example</span><span class="dot"></span></div>
</section>

<section class="piece folder folder-small">
  <div class="panel inside">
    <div class="brand"><span class="dot"></span>Harborline Motorworks</div>
    <div class="tiny" style="margin-top:6px;text-align:center">Phone 313.555.0142<br>Fax 313.555.0143</div>
    <div class="url">www.harborlinemotorworks.example</div>
  </div>
  <div class="panel cover">
    <svg viewBox="0 0 100 100" preserveAspectRatio="none" aria-hidden="true">
      <path d="M76 0 C92 30 92 70 78 100 L100 100 L100 0Z" fill="var(--black)"/>
      <path d="M83 0 C98 30 98 70 85 100 L100 100 L100 0Z" fill="var(--red)"/>
    </svg>
    <div class="brand"><span class="dot"></span>Harborline Motorworks</div>
    <div class="services">Dealer Services<br>Lead Generation<br>Website Development<br><br>4816 Pell Ave<br>Detroit, MI 48201</div>
  </div>
</section>

<section class="piece invoice invoice-small">
  <div class="head"><div class="brand"><span class="dot"></span>Harborline Motorworks</div><h2>INVOICE</h2></div>
  <div class="bar"><span>Qty</span><span>Description</span><span>Price</span><span>Total</span></div>
  <div class="table"><div></div><div></div><div></div><div></div></div>
  <div class="total"></div>
</section>

<section class="piece fax">
  <div class="head"><div class="brand"><span class="dot"></span>Harborline Motorworks</div><h2>FAX</h2></div>
  <div class="fields"><span>To</span><span>From</span><span>Date</span><span>Pages</span><span>Re</span><span></span></div>
  <div class="foot"></div>
</section>

<article class="piece card c1 r1">
  <div class="brand"><span class="dot"></span>Harborline Motorworks</div>
  <div class="who"><b>Marcus Delaney</b><span>President</span></div>
  <div class="contact">Phone 313.555.0142<br>Fax 313.555.0143<br>Cell 313.555.0144<br>mdelaney@harborlinemotorworks.example</div>
  <div class="band"></div>
</article>
<article class="piece card c2 r1">
  <div class="brand"><span class="dot"></span>Harborline Motorworks</div>
  <div class="who"><b>Marcus Delaney</b><span>President</span></div>
  <div class="contact">Phone 313.555.0142<br>Fax 313.555.0143<br>Cell 313.555.0144<br>mdelaney@harborlinemotorworks.example</div>
  <div class="band"></div>
</article>
<article class="piece card back dark c1 r2">
  <div class="seal"></div>
  <div class="list"><b>Dealer Services</b><br>Lead Generation<br>Website Development<br>Internet Sales Training</div>
  <div class="tag">Every Make. Every Model.<br>At The Lowest Price.</div>
</article>
<article class="piece card back red c2 r2">
  <div class="seal"></div>
  <div class="list"><b>Consumer Services</b><br>Unbiased Vehicle Information<br>Every Make. Every Model.<br>At The Lowest Price.</div>
  <div class="tag">Lead Generation<br>Website Development</div>
</article>
<article class="piece card round c1 r3">
  <div class="brand"><span class="dot"></span>Harborline Motorworks</div>
  <div class="who"><b>Marcus Delaney</b><span>President</span></div>
  <div class="contact">Phone 313.555.0142<br>Fax 313.555.0143<br>Cell 313.555.0144<br>mdelaney@harborlinemotorworks.example</div>
</article>
<article class="piece card round c2 r3">
  <div class="brand"><span class="dot"></span>Harborline Motorworks</div>
  <div class="who"><b>Marcus Delaney</b><span>President</span></div>
  <div class="contact">Phone 313.555.0142<br>Fax 313.555.0143<br>Cell 313.555.0144<br>www.harborlinemotorworks.example</div>
</article>

<section class="piece folder folder-large">
  <div class="panel inside">
    <div class="brand"><span class="dot"></span>Harborline Motorworks</div>
    <div class="tiny" style="margin-top:6px;text-align:center">Phone 313.555.0142<br>Fax 313.555.0143</div>
    <div class="url">www.harborlinemotorworks.example</div>
  </div>
  <div class="panel cover">
    <svg viewBox="0 0 100 100" preserveAspectRatio="none" aria-hidden="true">
      <path d="M0 0 L60 0 C20 25 15 60 0 80Z" fill="var(--black)"/>
      <path d="M50 0 L100 0 L100 35 C80 10 60 5 50 0Z" fill="var(--red)"/>
      <path d="M0 0 L45 0 C10 20 8 55 0 70Z" fill="var(--red)"/>
    </svg>
    <div class="brand"><span class="dot"></span>Harborline Motorworks</div>
    <div class="services">Dealer Services<br>Lead Generation<br>Website Development<br><br>4816 Pell Ave<br>Detroit, MI 48201</div>
  </div>
</section>

<section class="piece invoice invoice-large">
  <div class="head"><div class="brand"><span class="dot"></span>Harborline</div><h2>INVOICE</h2></div>
  <div class="bar"><span>Qty</span><span>Item</span><span>Total</span></div>
  <div class="table"><div></div><div></div><div></div><div></div></div>
  <div class="total"></div>
</section>

<section class="piece envelope env-front">
  <div class="brand"><span class="dot"></span>Harborline Motorworks</div>
  <div class="tiny" style="position:absolute;left:10px;top:26px">4816 Pell Ave<br>Detroit, MI 48201</div>
  <div class="seal"></div>
  <div class="band"></div>
</section>
<section class="piece envelope env-back">
  <svg viewBox="0 0 100 100" preserveAspectRatio="none" aria-hidden="true">
    <path d="M0 0 L50 45 L100 0" fill="none" stroke="#ccc" stroke-width=".6"/>
  </svg>
  <div class="seal"></div>
</section>

</body>
</html>
```